Business Card for Orvane Parts Wholesale supplier

Hi There! I need a new business card for our company. We are specialized in selling Orvane parts, mostly we sell new LCD screens for Telvox and Slatrons. I would like to see that back in the design.

You can find the colors and logo's on our website: www.dorvak-example.nl

Industry/Entity Type

Business

Contact Information for Business Card

My Details:
Lars Vintorp

Phone: 0031612873406
E-mail: Lars@dorvak-example.nl

Slogan: "Because Quality Matters"

Font styles to use
Sans Serif

Colors

Designer to choose colors to be used in the design.

Requirements
Must have
• A Black backside with the Dorvak logo on it. The front side should be clean with only my contact details.
• But I'm also open for something really different or awesome!
Nice to have
• Remember that we are in the parts & repairing industry, So i'll be handing those business cards mainly to repair companies. Maybe you can do something with that thought :)

```html
<!DOCTYPE html>
<html lang="en">
<head>
<meta charset="utf-8">
<title>Dorvak Business Card</title>
<link rel="stylesheet" href="https://fonts.googleapis.com/css2?family=Saira:wght@400;600;700&family=Open+Sans:wght@600&display=swap">
<style>
  :root {
    --backdrop: #5b4a3b;
    --card-white: #ffffff;
    --card-black: #050403;
    --accent: #f37021;
    --ink: #111111;
    --muted: #555555;
    --pattern-dark: #0b0806;
    --pattern-warm: #24170c;
  }
  * { margin: 0; padding: 0; box-sizing: border-box; }
  html, body {
    width: 1200px; height: 987px; overflow: hidden;
    background: var(--backdrop);
  }
  .stage { position: relative; width: 1200px; height: 987px; }
  .card {
    position: absolute; left: 293px; width: 615px; height: 352px;
    overflow: hidden;
    box-shadow: 0 3px 8px rgba(0,0,0,0.35);
  }
  .card--front { top: 130px; background: var(--card-white); }
  .card--back { top: 505px; background: var(--card-black); }

  .corner { position: absolute; }
  .corner--top { left: 0; top: 0; }
  .corner--bottom { right: 0; bottom: 0; }

  .brand {
    position: absolute; right: 50px; top: 40px;
    display: flex; align-items: center; gap: 12px;
  }
  .brand__dot { width: 54px; height: 54px; border-radius: 50%; background: var(--accent); }
  .brand__name {
    font-family: "Saira", sans-serif; font-weight: 700;
    font-size: 56px; line-height: 1; color: var(--ink); letter-spacing: 0.5px;
  }
  .holder {
    position: absolute; right: 52px; top: 124px;
    font-family: "Saira", sans-serif; font-weight: 600;
    font-size: 21px; color: var(--accent); letter-spacing: 0.5px;
  }
  .contacts {
    position: absolute; left: 50px; top: 240px; list-style: none;
    font-family: "Saira", sans-serif; font-size: 16px; color: var(--muted);
  }
  .contacts li { display: flex; align-items: center; gap: 8px; height: 23.5px; }
  .contacts svg { width: 15px; height: 15px; fill: var(--accent); flex: none; }

  .pattern {
    position: absolute; inset: 0;
    background: linear-gradient(160deg, var(--pattern-warm), var(--pattern-dark) 55%, var(--pattern-warm));
  }
  .back-brand {
    position: absolute; left: 0; right: 0; top: 158px; text-align: center;
    font-family: "Saira", sans-serif; font-weight: 700;
    font-size: 42px; line-height: 1; color: var(--accent);
  }
  .slogan {
    position: absolute; left: 0; right: 0; top: 276px; text-align: center;
    font-family: "Open Sans", sans-serif; font-weight: 600;
    font-size: 17.5px; color: #ffffff;
  }
</style>
</head>
<body>
<main class="stage">
  <section class="card card--front">
    <svg class="corner corner--top" width="104" height="104" viewBox="0 0 104 104" aria-hidden="true">
      <polygon points="0,0 104,0 0,104" fill="var(--accent)"/>
    </svg>
    <svg class="corner corner--bottom" width="104" height="105" viewBox="0 0 104 105" aria-hidden="true">
      <polygon points="104,0 104,105 0,105" fill="var(--card-black)"/>
    </svg>

    <div class="brand">
      <span class="brand__dot"></span>
      <span class="brand__name">Dorvak</span>
    </div>
    <p class="holder">LARS VINTORP</p>

    <ul class="contacts">
      <li>
        <svg viewBox="0 0 24 24" aria-hidden="true"><path d="M6.6 10.8a15.1 15.1 0 0 0 6.6 6.6l2.2-2.2c.3-.3.7-.4 1-.2 1.1.4 2.3.6 3.6.6.6 0 1 .4 1 1V20c0 .6-.4 1-1 1A17 17 0 0 1 3 4c0-.6.4-1 1-1h3.5c.6 0 1 .4 1 1 0 1.3.2 2.5.6 3.6.1.3 0 .7-.2 1z"/></svg>
        <span>0031612873406</span>
      </li>
      <li>
        <svg viewBox="0 0 24 24" aria-hidden="true"><path d="M2 5h20v14H2z M2 5l10 8 10-8" fill="none" stroke="var(--accent)" stroke-width="0"/><path d="M2 6.5 12 13l10-6.5V19H2z"/><path d="M2 5h20l-10 6.5z"/></svg>
        <span>Lars@dorvak-example.nl</span>
      </li>
      <li>
        <svg viewBox="0 0 24 24" aria-hidden="true"><circle cx="12" cy="12" r="10"/><path d="M7 6c2 1 1 3 3 4s1 3 0 4 1 3 0 5M15 4c-1 2 1 3 3 3s2 2 3 3M14 13c2-1 4 0 4 2s-2 3-3 5" fill="none" stroke="#fff" stroke-width="1.5"/></svg>
        <span>www.dorvak-example.nl</span>
      </li>
    </ul>
  </section>

  <section class="card card--back">
    <div class="pattern" role="img" aria-label="Repeating dark brown brand pattern across the black back side"></div>
    <p class="back-brand">Dorvak</p>
    <p class="slogan">Because Quality Matters</p>
  </section>
</main>
</body>
</html>
```